Shotcrete Contractor Needs Business Cards Designed

We're a Shotcrete construction company based out of Southern California who opened another office in Northern California and needs new cards. The cards need to have our logo,name,title,license #,contact info, and website. Both office locations need to be on the card as well. We are looking for a professional clean design that will work well in the construction industry. PLEASE VISIT THE WEBSITE to get a feel about the company. www.ridgelinegunite.example

Industry/Entity Type

Construction

```html
<!DOCTYPE html>
<html lang="en">
<head>
<meta charset="utf-8">
<title>Ridgeline Gunite Incorporated – Business Cards</title>
<link href="https://fonts.googleapis.com/css2?family=Roboto:wght@400;500;700&display=swap" rel="stylesheet">
<style>
  :root {
    --bg: #ececec;
    --card: #f7f7f7;
    --navy: #2c2a78;
    --red: #a93432;
    --ink: #555555;
    --rule: #9a9a9a;
  }
  * { box-sizing: border-box; margin: 0; padding: 0; }
  html, body { width: 1200px; height: 1001px; overflow: hidden; }
  body {
    background: var(--bg);
    font-family: "Roboto", Arial, sans-serif;
    display: flex;
    align-items: center;
    justify-content: center;
    gap: 60px;
  }
  .card {
    position: relative;
    width: 520px;
    height: 297px;
    background: var(--card);
    box-shadow: 0 6px 18px rgba(0,0,0,0.12);
    overflow: hidden;
  }
  .card__band {
    position: absolute;
    left: 0; right: 0; bottom: 0;
    height: 7px;
    background: var(--red);
  }

  /* Contact side */
  .contact { display: flex; }
  .contact__brand {
    width: 220px;
    display: flex;
    align-items: center;
    justify-content: center;
    gap: 12px;
    padding-bottom: 20px;
  }
  .brand-square { width: 22px; height: 22px; background: var(--red); flex: none; }
  .brand-name {
    color: var(--navy);
    font-weight: 700;
    font-size: 17px;
    line-height: 1.25;
    letter-spacing: 0.5px;
  }
  .contact__divider {
    width: 1px;
    background: var(--rule);
    margin: 30px 0 40px;
  }
  .contact__details {
    padding: 24px 0 0 24px;
    color: var(--ink);
    font-size: 12.5px;
    line-height: 1.38;
  }
  .person__name { color: var(--red); font-weight: 700; font-size: 20px; line-height: 1.1; }
  .person__title { font-size: 12.5px; margin-bottom: 8px; }
  .office { margin-bottom: 4px; }
  .office__label { color: var(--red); font-weight: 700; }
  .detail__label { color: var(--red); font-weight: 700; display: inline-block; width: 30px; }

  /* Name side */
  .identity {
    display: flex;
    flex-direction: column;
    align-items: center;
    justify-content: center;
    gap: 14px;
    padding-bottom: 10px;
  }
  .identity__square { width: 46px; height: 46px; background: var(--red); }
  .identity__name {
    color: var(--navy);
    font-weight: 700;
    font-size: 27px;
    letter-spacing: 1px;
    text-align: center;
    line-height: 1.2;
  }
</style>
</head>
<body>
  <section class="card contact">
    <div class="contact__brand">
      <span class="brand-square"></span>
      <span class="brand-name">RIDGELINE<br>GUNITE INC.</span>
    </div>
    <div class="contact__divider"></div>
    <div class="contact__details">
      <p class="person__name">Your Name</p>
      <p class="person__title">Manager</p>
      <div class="office">
        <p><span class="office__label">SoCal:</span> 4410 Canyon Ridge Road, Suite 120,</p>
        <p>Valencia, CA 91355</p>
      </div>
      <div class="office">
        <p><span class="office__label">NorCal:</span> 2150 Harbor Point Drive, Suite 8,</p>
        <p>Sacramento, CA 95815</p>
      </div>
      <p><span class="detail__label">T -</span>(555) 014-2290</p>
      <p><span class="detail__label">F -</span>555-014-2291</p>
      <p><span class="detail__label">E -</span>info@ridgelinegunite.example</p>
      <p><span class="detail__label">W-</span>www.ridgelinegunite.example</p>
      <p><span class="detail__label">CA -</span>License # 100482</p>
    </div>
    <div class="card__band"></div>
  </section>

  <section class="card identity">
    <span class="identity__square"></span>
    <p class="identity__name">RIDGELINE GUNITE<br>INCORPORATED</p>
    <div class="card__band"></div>
  </section>
</body>
</html>
```